New Flyer Design Project - for sale units at The Lodge phase 3

on attached the A2 is full kitchen 1 bedroom, the A3 is gally kitchen and the B2 is the the 2 bedroom, on attached pictures the room with 2 queen beds is only for the 2 bedroom

This is going to be used to sale the units (real estate sale) so the layout could possibly be text and then pictures maybe 1 bedroom on one side and 2 on the back?

Experience the Modern Luxury of the New Phase 3 Building of the
Lodge at Harlow Bend

* Opening Spring 2019

* America's #17 Family Resort; Tennessee's Only Ranked Resort

1 Bedroom Bunk Suite (Galley Kitchen) - $199,000; Sleeps 6

* Private King Master Bedroom

* Bunk Bed Galley

* Granite Counters Throughout

* Fully Furnished with Custom Furnishings

* Private Balcony

* Equipped Galley Kitchen

* In Unit Laundry

* Queen Sleeper Sofa

1 Bedroom Bunk Suite (Full Kitchen) - $209,000; Sleeps 6

* Bunk Bed Galley

* Granite Counters throughout

* Equipped Full Kitchen

* Completely Furnished with Custom Furnishings

* Private Balcony

* In Unit Laundry

* Queen Sleeper Sofa

2 Bedroom Bunk Suite (Full Kitchen) - $249,000; Sleeps 10

* Private King Master Bedroom with On-Suite Bathroom

* Two Queen Bedroom

* Bunk Bed Galley

* Full Kitchen

* Private Balcony

* In Unit Laundry

* Queen Sleeper Sofa

Target Market(s)

people wanting to buy units in phase 3 of The Lodge at Harlow Bend

Industry/Entity Type

Real Estate Development

Requirements
Must have
• attached text to describe units and price
• pictures and layouts
• Contact Dale Porter
• 865-730-2958 Dale@brightfernretreats.example
Nice to have
• brand and logo
Should not have
• it should not be plain this is m ore of a luxury project

```html
<!DOCTYPE html>
<html lang="en">
<head>
<meta charset="utf-8">
<title>Phase 3 Suites — The Lodge at Harlow Bend</title>
<link href="https://fonts.googleapis.com/css2?family=Libre+Baskerville:wght@400;700&family=Open+Sans:wght@400;600&display=swap" rel="stylesheet">
<style>
  :root {
    --slate: #587884;
    --amber: #e69d3f;
    --navy: #2c4656;
    --ink: #3d4a52;
    --paper: #ffffff;
    --footer: #5d7784;
    --plan-bg: #f6f3ec;
  }
  * { margin: 0; padding: 0; box-sizing: border-box; }
  html, body { width: 849px; height: 1200px; overflow: hidden; background: var(--paper); }
  .flyer { position: relative; width: 849px; height: 1200px; font-family: "Open Sans", Arial, sans-serif; color: var(--ink); }

  .plans { position: absolute; top: 0; left: 0; width: 849px; height: 270px; display: flex; }
  .plans__panel { flex: 1; display: flex; align-items: center; justify-content: center; }
  .plans__panel--one { background: var(--slate); }
  .plans__panel--two { background: var(--amber); }
  .plans__drawing { width: 300px; height: 236px; border: 2px solid #fff;
    background:
      radial-gradient(ellipse at 30% 35%, rgba(72,110,150,.35), transparent 40%),
      radial-gradient(ellipse at 62% 65%, rgba(196,120,60,.35), transparent 38%),
      linear-gradient(160deg, var(--plan-bg), #e2dccf); }

  .suite { position: absolute; top: 282px; width: 400px; }
  .suite--one { left: 38px; }
  .suite--two { left: 462px; }
  .suite__title { font-family: "Libre Baskerville", Georgia, serif; font-weight: 700; font-size: 20px; color: var(--navy); line-height: 1.3; }
  .suite__title small { font-size: 12.5px; }
  .suite__price { font-family: "Libre Baskerville", Georgia, serif; font-weight: 700; font-size: 24px; color: var(--navy); margin-top: 2px; }
  .suite__price small { font-size: 14px; }
  .features { list-style: none; margin-top: 20px; }
  .features li { position: relative; padding-left: 18px; font-size: 14px; line-height: 26px; }
  .features li::before { content: ""; position: absolute; left: 0; top: 10px; width: 6px; height: 6px; border-radius: 50%; background: var(--amber); }
  .features li.cont { line-height: 18px; margin-top: -5px; padding-bottom: 4px; }
  .features li.cont::before { display: none; }

  .photos { position: absolute; top: 640px; left: 0; width: 849px; height: 424px; display: flex; gap: 6px; }
  .photo { position: relative; }
  .photo--bedroom { width: 497px;
    background:
      radial-gradient(ellipse at 55% 70%, rgba(245,240,228,.85), transparent 35%),
      linear-gradient(90deg, #a9b79a 0%, #c9d2c0 25%, #d3d8cb 60%, #b7c2ac 100%); }
  .photo--bedroom::after { content: ""; position: absolute; left: 0; right: 0; bottom: 0; height: 30%; background: linear-gradient(180deg, rgba(110,90,72,0), #6b5646); }
  .photo--bath { flex: 1;
    background:
      radial-gradient(ellipse at 30% 60%, rgba(250,250,248,.8), transparent 30%),
      linear-gradient(180deg, #d4dccb 0%, #c1cbb5 55%, #5a4639 80%, #4a3a30 100%); }
  .photo__label { position: absolute; top: 10px; right: 14px; z-index: 1; font-size: 10px; letter-spacing: 1px; text-transform: uppercase; color: #fff; }

  .contact-bar { position: absolute; top: 1072px; left: 0; width: 849px; height: 128px; background: var(--footer); display: flex; align-items: center; padding-left: 24px; }
  .brand { width: 130px; display: flex; flex-direction: column; align-items: center; gap: 8px; }
  .brand__mark { width: 14px; height: 14px; background: var(--amber); }
  .brand__name { font-family: "Libre Baskerville", Georgia, serif; font-weight: 700; font-size: 19px; color: #fff; }
  .contact { margin-left: 110px; color: #fff; font-family: "Libre Baskerville", Georgia, serif; font-size: 17px; line-height: 34px; }
  .contact b { font-weight: 700; }
</style>
</head>
<body>
<main class="flyer">
  <section class="plans">
    <div class="plans__panel plans__panel--one">
      <div class="plans__drawing" role="img" aria-label="Floor plan of the 1 bedroom bunk suite with full kitchen"></div>
    </div>
    <div class="plans__panel plans__panel--two">
      <div class="plans__drawing" role="img" aria-label="Floor plan of the 2 bedroom bunk suite with full kitchen"></div>
    </div>
  </section>

  <section class="suite suite--one">
    <h2 class="suite__title">1 Bedroom Bunk Suite <small>(Full Kitchen)</small></h2>
    <p class="suite__price">$209,000 <small>(Sleeps 6)</small></p>
    <ul class="features">
      <li>Private King Master Bedroom</li>
      <li>Bunk Bed Galley</li>
      <li>Granite Counters throughout</li>
      <li>Equipped Full Kitchen</li>
      <li>Completely Furnished with Custom Furnishings</li>
      <li>Private Balcony</li>
      <li>In Unit Laundry</li>
      <li>Queen Sleeper Sofa</li>
    </ul>
  </section>

  <section class="suite suite--two">
    <h2 class="suite__title">2 Bedroom Bunk Suite <small>(Full Kitchen)</small></h2>
    <p class="suite__price">$249,000 <small>(Sleeps 10)</small></p>
    <ul class="features">
      <li>Private King Master Bedroom</li>
      <li class="cont">with On-Suite Bathroom</li>
      <li>Two Queen Bedroom</li>
      <li>Bunk Bed Galley</li>
      <li>Granite Counters Throughout</li>
      <li>Full Kitchen</li>
      <li>Completely Furnished with Custom Furnishings</li>
      <li>Private Balcony</li>
      <li>In Unit Laundry</li>
    </ul>
  </section>

  <section class="photos">
    <div class="photo photo--bedroom" role="img" aria-label="King bedroom with bed, lamps and nightstands">
      <span class="photo__label">King Bedroom</span>
    </div>
    <div class="photo photo--bath" role="img" aria-label="Bathroom with vanity, mirror and bathtub">
      <span class="photo__label">Bathroom</span>
    </div>
  </section>

  <footer class="contact-bar">
    <div class="brand">
      <span class="brand__mark"></span>
      <span class="brand__name">The Lodge</span>
    </div>
    <div class="contact">
      <p>Contact: <b>Dale Porter</b></p>
      <p>Call: <b>865-730-2958</b> &nbsp;Email: <b>Dale@brightfernretreats.example</b></p>
    </div>
  </footer>
</main>
</body>
</html>
```